Corinne Hale

I need a label design for a Woman's Professional Haircare line sold to salons. So the label would be on Shampoo's, Conditioners , serum's, styling products, bleaches, etc...
I'm looking at a softer color label design like lavender or shades of lighter purple. i would like Logo to be or contain a rose rose. Here are a few designs from the professional ranks that are different. They use the solid colors with the back design. I was thinking something like this might work.

Colors
A7469A
B969AE
D3A5CF
EDDBEB
F8F0F9
6B429C
8869AF
B7A5CE
E3DAEB
F3F0F8

```html
<!DOCTYPE html>
<html lang="en">
<head>
<meta charset="UTF-8">
<title>Corinne Hale — Volume and Thickening Shampoo</title>
<link rel="stylesheet" href="https://fonts.googleapis.com/css2?family=Josefin+Sans:wght@300;400&family=Montserrat:wght@400&display=swap">
<style>
  :root {
    --page: #ffffff;
    --lavender-body: #b49bd4;
    --lavender-cap: #a78bcf;
    --lavender-art-a: #6b429c;
    --lavender-art-b: #8869af;
    --berry-body: #a7469a;
    --berry-cap: #c466b6;
    --berry-art-a: #5e1f58;
    --berry-art-b: #7e2f76;
    --label-white: #f8f0f9;
  }
  * { margin: 0; padding: 0; box-sizing: border-box; }
  html, body { width: 847px; height: 1200px; overflow: hidden; background: var(--page); }
  .canvas { position: relative; width: 847px; height: 1200px; }

  .bottle { position: absolute; top: 100px; width: 283px; height: 1000px; }
  .bottle--lavender { left: 110px; }
  .bottle--berry { left: 454px; }
  .bottle__shape { position: absolute; inset: 0; }

  .fill-body--lavender { fill: var(--lavender-body); }
  .fill-cap--lavender { fill: var(--lavender-cap); }
  .fill-body--berry { fill: var(--berry-body); }
  .fill-cap--berry { fill: var(--berry-cap); }

  .brand {
    position: absolute; top: 325px; left: 0; width: 100%;
    text-align: center; color: var(--label-white);
    font-family: "Josefin Sans", sans-serif; line-height: 1;
  }
  .brand__first { display: block; font-size: 40px; font-weight: 300; letter-spacing: 0; }
  .brand__last { display: block; font-size: 72px; font-weight: 400; letter-spacing: 3px; margin-top: 4px; }

  .rose-art {
    position: absolute; top: 480px; left: 50%; transform: translateX(-50%);
    width: 200px; height: 350px;
  }

  .product {
    position: absolute; top: 848px; left: 0; width: 100%;
    text-align: center; color: var(--label-white);
    font-family: "Montserrat", sans-serif; font-weight: 400;
    font-size: 13px; letter-spacing: 0.5px; line-height: 1.35;
    text-transform: uppercase;
  }
  .volume {
    position: absolute; top: 935px; left: 0; width: 100%;
    text-align: center; color: var(--label-white);
    font-family: "Montserrat", sans-serif; font-size: 12px; letter-spacing: 0.4px;
  }
</style>
</head>
<body>
<main class="canvas">

  <article class="bottle bottle--lavender">
    <svg class="bottle__shape" viewBox="0 0 283 1000" width="283" height="1000" aria-hidden="true">
      <path class="fill-body--lavender" d="M80 125 L203 125 C255 140 283 180 283 240 L283 980 Q283 1000 263 1000 L20 1000 Q0 1000 0 980 L0 240 C0 180 28 140 80 125 Z"/>
      <path class="fill-cap--lavender" d="M88 4 Q88 0 94 0 L189 0 Q195 0 195 4 L200 127 L83 127 Z"/>
    </svg>
    <h2 class="brand"><span class="brand__first">CORINNE</span><span class="brand__last">HALE</span></h2>
    <svg class="rose-art" viewBox="0 0 200 350" role="img" aria-label="Line illustration of a bouquet of long-stemmed roses with leaves">
      <defs>
        <radialGradient id="roseLavender" cx="0.5" cy="0.35" r="0.6">
          <stop offset="0" stop-color="#6b429c" stop-opacity="0.45"/>
          <stop offset="0.6" stop-color="#8869af" stop-opacity="0.25"/>
          <stop offset="1" stop-color="#8869af" stop-opacity="0"/>
        </radialGradient>
      </defs>
      <rect width="200" height="350" fill="url(#roseLavender)"/>
    </svg>
    <p class="product">Volume and<br>thickening shampoo</p>
    <p class="volume">300 ML / 10 US FL OZ</p>
  </article>

  <article class="bottle bottle--berry">
    <svg class="bottle__shape" viewBox="0 0 283 1000" width="283" height="1000" aria-hidden="true">
      <path class="fill-body--berry" d="M80 125 L203 125 C255 140 283 180 283 240 L283 980 Q283 1000 263 1000 L20 1000 Q0 1000 0 980 L0 240 C0 180 28 140 80 125 Z"/>
      <path class="fill-cap--berry" d="M88 4 Q88 0 94 0 L189 0 Q195 0 195 4 L200 127 L83 127 Z"/>
    </svg>
    <h2 class="brand"><span class="brand__first">CORINNE</span><span class="brand__last">HALE</span></h2>
    <svg class="rose-art" viewBox="0 0 200 350" role="img" aria-label="Line illustration of a bouquet of long-stemmed roses with leaves">
      <defs>
        <radialGradient id="roseBerry" cx="0.5" cy="0.35" r="0.6">
          <stop offset="0" stop-color="#5e1f58" stop-opacity="0.5"/>
          <stop offset="0.6" stop-color="#7e2f76" stop-opacity="0.28"/>
          <stop offset="1" stop-color="#7e2f76" stop-opacity="0"/>
        </radialGradient>
      </defs>
      <rect width="200" height="350" fill="url(#roseBerry)"/>
    </svg>
    <p class="product">Volume and<br>thickening shampoo</p>
    <p class="volume">300 ML / 10 US FL OZ</p>
  </article>

</main>
</body>
</html>
```